Quarry Lane Co. needs Business Cards

For this project, we need business cards (currently have also put a call out for a logo). We are a start-up called Quarry Lane Co. This is our second company (our first one was called Brightwickery). Traditionally we have been providing market research services across different sectors, primarily financial services and the pharmaceutical industry. However, we now want to go beyond market research to offer more (Etc.)... strategic consulting and big data knowledge management. We want our brand to be approachable, creative, fun but professional.

Target Market(s)

The target audience is a business professional - we are B2B (business to business) and do not sell our services to individuals. The brands we work with are major brands across industries, but primarily automotive, financial and pharmaceutical.

Industry/Entity Type

Market Research

Font styles to use
Serif
Sans Serif
Other font styles liked:
• Calibri

Requirements
Must have
• Be clean, simple, modern
Show our address and phone number and email address and website URL
We do not need to have titles showing.

```html
<!DOCTYPE html>
<html lang="en">
<head>
<meta charset="utf-8">
<title>Quarry Lane Co. — Business Card</title>
<link rel="stylesheet" href="https://fonts.googleapis.com/css2?family=Carlito:ital,wght@0,400;0,700;1,700&display=swap">
<style>
  :root {
    --backdrop: #dcdcdc;
    --card-grey: #4a4a4a;
    --brand-red: #760011;
    --paper-white: #efefed;
    --ink: #111111;
    --card-w: 800px;
    --card-h: 457px;
  }
  * { box-sizing: border-box; margin: 0; padding: 0; }
  html, body {
    width: 1200px;
    height: 1000px;
    overflow: hidden;
    background: var(--backdrop);
    font-family: "Carlito", "Calibri", sans-serif;
  }
  .sheet {
    width: 1200px;
    height: 1000px;
    display: flex;
    flex-direction: column;
    align-items: center;
    justify-content: center;
    gap: 36px;
  }
  .card {
    position: relative;
    width: var(--card-w);
    height: var(--card-h);
    background: var(--card-grey);
    overflow: hidden;
    box-shadow: 0 2px 6px rgba(0,0,0,0.18);
  }

  /* Front: brand band */
  .front .tab-left {
    position: absolute;
    left: 0; top: 14%;
    width: 17%; height: 22%;
    background: var(--brand-red);
  }
  .front .name-band {
    position: absolute;
    left: 17%; top: 17%;
    width: 71%; height: 24%;
    background: var(--paper-white);
    display: flex;
    align-items: center;
    justify-content: center;
  }
  .front .tab-right {
    position: absolute;
    right: 0; top: 21%;
    width: 12%; height: 23%;
    background: var(--brand-red);
  }
  .company-name {
    color: var(--brand-red);
    font-weight: 700;
    font-size: 62px;
    letter-spacing: 0.5px;
  }

  /* Back: person and contact */
  .back .person-block {
    position: absolute;
    left: 9%; top: 21%;
    width: 46%; height: 28%;
    background: var(--brand-red);
    display: flex;
    align-items: center;
    justify-content: center;
  }
  .person-name {
    color: var(--paper-white);
    font-weight: 700;
    font-style: italic;
    font-size: 44px;
  }
  .back .contact-block {
    position: absolute;
    left: 58%; top: 38%;
    width: 40%; height: 36%;
    background: var(--paper-white);
    padding: 22px 28px;
    display: flex;
    flex-direction: column;
    justify-content: center;
    gap: 8px;
  }
  .contact-line {
    color: var(--ink);
    font-size: 24px;
    line-height: 1.15;
    white-space: nowrap;
  }
</style>
</head>
<body>
  <main class="sheet">
    <section class="card front" aria-label="Card front">
      <div class="tab-left"></div>
      <div class="name-band">
        <h1 class="company-name">Quarry Lane Co.</h1>
      </div>
      <div class="tab-right"></div>
    </section>

    <section class="card back" aria-label="Card back">
      <div class="person-block">
        <p class="person-name">Your Name</p>
      </div>
      <div class="contact-block">
        <p class="contact-line">P : 012- 345- 6789</p>
        <p class="contact-line">E : your name@mail.com</p>
        <p class="contact-line">W : www.address.com</p>
      </div>
    </section>
  </main>
</body>
</html>
```